Zielgruppe
System- und Netzwerkadministration
IT Sicherheit
Datenrettung und Backuplösungen
Web-Entwicklung und Betreuung
Sicherheits- und Überwachungstechnik
Heimnetzwerk und Entertainment
Zielgruppe:
kleine und mittelständische Unternehmen
Arztpraxen und Heilpraktiker
ggf. auch Privatpersonen
Aufgabenstellung
Hauptsitz in Fürth:
TH IT-Service - Ahrenfeld • Kellersbach • Wiesbrunn
Friedrich Haberkorn
Wendelin-Marbach-Straße 7c
41673 Kellersbach
Zweigstelle in Ahrenfeld:
Untere Pappelgasse 4
41628 Ahrenfeld
E-Mail: service@datwerk-hilfe.example
Hotline: +49 151 - 47290815
Steuernummer: 304/592/17830
Kein Steuerausweis aufgrund der Anwendung der Kleinunternehmerregelung (

```html
<!DOCTYPE html>
<html lang="de">
<head>
<meta charset="utf-8">
<title>TH IT-Service – Logo und Geschäftsausstattung</title>
<link href="https://fonts.googleapis.com/css2?family=Open+Sans:wght@400;600;700&display=swap" rel="stylesheet">
<style>
  :root {
    --ink: #3d3d3f;
    --blue: #1a9ae0;
    --paper: #ffffff;
    --panel-light: #ebebed;
    --stage: #e4e4e6;
    --muted: #6c6c70;
    --rule: #9a9a9e;
    --web-grey: #c9c9cc;
  }
  * { box-sizing: border-box; margin: 0; padding: 0; }
  html, body { width: 1200px; height: 736px; overflow: hidden; }
  body { font-family: "Open Sans", sans-serif; color: var(--ink); background: var(--stage); position: relative; }

  .logo-column { position: absolute; left: 0; top: 0; width: 453px; height: 736px; }
  .logo-panel { height: 245.33px; display: flex; align-items: center; justify-content: center; gap: 12px; }
  .logo-panel--white { background: var(--paper); }
  .logo-panel--light { background: var(--panel-light); }
  .logo-panel--dark { background: var(--ink); }
  .wordmark { font-weight: 600; font-size: 46px; letter-spacing: -0.5px; color: var(--ink); white-space: nowrap; }
  .logo-panel--dark .wordmark { color: var(--paper); }
  .wordmark-square { width: 14px; height: 14px; background: var(--blue); flex: none; }

  .sheet { position: absolute; background: var(--paper); box-shadow: 0 6px 18px rgba(0,0,0,.12); }
  .small-mark { display: flex; align-items: center; gap: 5px; font-weight: 600; color: var(--ink); white-space: nowrap; }
  .small-mark .wordmark-square { width: 6px; height: 6px; }

  .letterhead { left: 830px; top: 30px; width: 320px; height: 452px; padding: 22px 24px; font-size: 5.6px; line-height: 1.55; }
  .letterhead .small-mark { font-size: 15px; justify-content: flex-end; }
  .letter-date { text-align: right; margin-top: 22px; color: var(--muted); }
  .letter-greeting { font-weight: 600; margin: 10px 0 6px; }
  .letter-body p { margin-bottom: 5px; padding-left: 6px; position: relative; }
  .letter-body p::before { content: "•"; position: absolute; left: 0; }
  .letter-sender { color: var(--blue); font-weight: 600; font-size: 6.5px; margin-top: 12px; }
  .signature { width: 70px; height: 20px; margin-top: 4px; background: linear-gradient(90deg, #d8d8da, #f2f2f3); }

  .letter-footer, .envelope-footer { position: absolute; left: 24px; right: 24px; bottom: 18px; display: flex; justify-content: space-between; font-size: 5.2px; line-height: 1.5; color: var(--ink); white-space: nowrap; }
  .footer-block { padding-left: 6px; border-left: 0.6px solid var(--rule); }
  .footer-block:first-child { border-left: none; padding-left: 0; }
  .contact-line { display: flex; align-items: center; gap: 3px; justify-content: flex-end; white-space: nowrap; }
  .dot { width: 4px; height: 4px; border-radius: 50%; background: var(--blue); display: inline-block; flex: none; }

  .card { width: 200px; height: 110px; padding: 10px 12px; font-size: 4.8px; line-height: 1.5; }
  .card--front { left: 490px; top: 70px; }
  .card--back { left: 490px; top: 200px; background: var(--ink); display: flex; flex-direction: column; align-items: center; justify-content: center; gap: 10px; }
  .card .small-mark { font-size: 12px; justify-content: center; }
  .card--back .small-mark { color: var(--paper); }
  .card-web { color: var(--web-grey); font-size: 7px; letter-spacing: 1.6px; white-space: nowrap; }
  .card-person { text-align: center; margin-top: 8px; font-size: 6.5px; font-weight: 600; }
  .card-role { color: var(--blue); font-weight: 400; font-size: 5.5px; }
  .card-details { display: flex; justify-content: space-between; margin-top: 8px; white-space: nowrap; }

  .envelope { left: 490px; top: 360px; width: 310px; height: 170px; padding: 16px 18px; }
  .envelope .small-mark { font-size: 13px; }
  .envelope-window { position: absolute; right: 22px; top: 70px; width: 112px; height: 50px; border-radius: 8px; background: #efeff0; }
  .envelope-footer { left: 18px; right: 18px; bottom: 14px; font-size: 4.8px; }
</style>
</head>
<body>
  <section class="logo-column">
    <div class="logo-panel logo-panel--white"><span class="wordmark-square"></span><span class="wordmark">TH IT-Service</span></div>
    <div class="logo-panel logo-panel--light"><span class="wordmark-square"></span><span class="wordmark">TH IT-Service</span></div>
    <div class="logo-panel logo-panel--dark"><span class="wordmark-square"></span><span class="wordmark">TH IT-Service</span></div>
  </section>

  <article class="sheet letterhead">
    <div class="small-mark"><span class="wordmark-square"></span>TH IT-Service</div>
    <div class="letter-date">Datum ____________</div>
    <div class="letter-greeting">Sehr geehrte Damen und Herren,</div>
    <div class="letter-body">
      <p>Mit dieser Bestellung beauftragen Sie uns mit der Einrichtung Ihres Netzwerks gemäß den vereinbarten Leistungen.</p>
      <p>Änderungen am Auftrag sind bis spätestens drei Werktage vor dem vereinbarten Termin schriftlich mitzuteilen.</p>
      <p>Die Installation erfolgt zum vereinbarten Termin, sofern alle notwendigen Zugänge vor Ort bereitstehen.</p>
      <p>Geräte bleiben bis zur vollständigen Bezahlung der Rechnung unser Eigentum.</p>
      <p>Für Schäden durch unsachgemäße Nutzung oder höhere Gewalt übernehmen wir keine Haftung.</p>
      <p>Reklamationen sind innerhalb von vierzehn Tagen nach Abschluss der Arbeiten anzuzeigen.</p>
    </div>
    <div class="letter-sender">Your Name HERE</div>
    <div class="signature" role="img" aria-label="Handschriftliche Unterschrift"></div>
    <footer class="letter-footer">
      <div class="footer-block">TH IT-Service<br>Ahrenfeld • Kellersbach • Wiesbrunn<br>Friedrich Haberkorn<br>Wendelin-Marbach-Straße 7c<br>41673 Kellersbach</div>
      <div class="footer-block">Zweigstelle in Ahrenfeld<br>TH IT-Service<br>Friedrich Haberkorn<br>Untere Pappelgasse 4<br>41628 Ahrenfeld</div>
      <div class="footer-block">
        <div class="contact-line">+49 151 - 47290815 <span class="dot"></span></div>
        <div class="contact-line">service@datwerk-hilfe.example <span class="dot"></span></div>
        <div class="contact-line">www.datwerk-hilfe.example <span class="dot"></span></div>
        <div class="contact-line">Steuernummer 304/592/17830</div>
      </div>
    </footer>
  </article>

  <article class="sheet card card--front">
    <div class="small-mark"><span class="wordmark-square"></span>TH IT-Service</div>
    <div class="card-person">Your Name HERE<br><span class="card-role">Manager</span></div>
    <div class="card-details">
      <div><strong>TH IT-Service</strong><br>Friedrich Haberkorn<br>Wendelin-Marbach-Straße 7c<br>41673 Kellersbach</div>
      <div>
        <div class="contact-line">+49 151 - 47290815 <span class="dot"></span></div>
        <div class="contact-line">service@datwerk-hilfe.example <span class="dot"></span></div>
        <div class="contact-line">www.datwerk-hilfe.example <span class="dot"></span></div>
      </div>
    </div>
  </article>

  <article class="sheet card card--back">
    <div class="small-mark"><span class="wordmark-square"></span>TH IT-Service</div>
    <div class="card-web">www.datwerk-hilfe.example</div>
  </article>

  <article class="sheet envelope">
    <div class="small-mark"><span class="wordmark-square"></span>TH IT-Service</div>
    <div class="envelope-window"></div>
    <footer class="envelope-footer">
      <div class="footer-block">TH IT-Service<br>Friedrich Haberkorn<br>Wendelin-Marbach-Straße 7c<br>41673 Kellersbach</div>
      <div class="footer-block">Zweigstelle in Ahrenfeld<br>Untere Pappelgasse 4<br>41628 Ahrenfeld</div>
      <div class="footer-block">
        <div class="contact-line">+49 151 - 47290815 <span class="dot"></span></div>
        <div class="contact-line">service@datwerk-hilfe.example <span class="dot"></span></div>
        <div class="contact-line">Steuernummer 304/592/17830</div>
      </div>
    </footer>
  </article>
</body>
</html>
```